Help keep hoosiers happy and at home!

We need a billboard designed for our Indiana based healthcare business called 'Harbor Lane Home Aides'. We administer a medicaid waiver program that provides support and financial aid to live in caregivers that take care of someone who would otherwise be in a nursing home or skilled nursing facility. Qualified caregivers could be eligible to receive up to 1200 dollars a month in tax free financial aid, as well as access to nursing support that helps manage any unexpected situations or changes in a care recipients condition or care routine. Our program empowers families to keep their loved ones at home and out of the nursing home. NOTE: We believe the tagline at the bottom of our logo is disproportionately small. We would like to see that tagline larger and easier to read. I look forward to seeing your design ideas!

Target Market(s)

Medicaid aged beneficiaries and caregivers.

Industry/Entity Type

Home Healthcare

Colors
0054AA
0677BA
7BADD7
CADEEF
E8F1F8

Requirements
Nice to have
• "Empowering friends and family to care for their loves ones at home. Eligible participants receive up to $15,000 a year, tax free."

```html
<!DOCTYPE html>
<html lang="en">
<head>
<meta charset="utf-8">
<title>Harbor Lane Home Aides – Billboard</title>
<link rel="stylesheet" href="https://fonts.googleapis.com/css2?family=Outfit:wght@500;600;700&display=swap">
<style>
  :root {
    --page-bg: #eef2f8;
    --brand-deep: #0054aa;
    --brand-mid: #0677ba;
    --brand-soft: #7badd7;
    --brand-pale: #cadeef;
    --brand-mist: #e8f1f8;
    --panel-dark: #1c4596;
    --white: #ffffff;
    --photo-warm: #f2d34a;
  }
  html, body {
    margin: 0;
    padding: 0;
    width: 1050px;
    height: 1200px;
    overflow: hidden;
    background: var(--page-bg);
    font-family: "Outfit", "Helvetica Neue", Arial, sans-serif;
  }
  .billboard {
    position: absolute;
    left: 25px;
    top: 350px;
    width: 1000px;
    height: 500px;
    overflow: hidden;
    box-shadow: 0 10px 28px rgba(10, 40, 90, 0.25);
    background: var(--brand-deep);
  }
  .billboard-art {
    position: absolute;
    inset: 0;
    width: 1000px;
    height: 500px;
  }
  .brand-name {
    position: absolute;
    left: 418px;
    top: 58px;
    width: 190px;
    margin: 0;
    color: var(--white);
    font-weight: 600;
    font-size: 25px;
    line-height: 1.08;
    text-align: center;
  }
  .headline {
    position: absolute;
    left: 620px;
    top: 28px;
    margin: 0;
    color: var(--white);
    font-weight: 700;
    font-size: 60px;
    line-height: 1.05;
    letter-spacing: -0.5px;
  }
  .headline .line-two { display: block; margin-left: -16px; }
  .mission {
    position: absolute;
    left: 470px;
    top: 200px;
    width: 500px;
    margin: 0;
    color: var(--white);
    font-weight: 600;
    font-size: 28px;
    line-height: 1.32;
    text-align: center;
  }
  .offer {
    position: absolute;
    left: 490px;
    top: 360px;
    width: 490px;
    margin: 0;
    color: var(--white);
    font-weight: 600;
    text-align: center;
  }
  .offer-lead { display: block; font-size: 29px; line-height: 1.2; }
  .offer-amount-row {
    display: flex;
    align-items: center;
    justify-content: center;
    gap: 10px;
    margin-top: 6px;
  }
  .offer-upto { font-size: 29px; margin-top: 16px; }
  .offer-amount { font-size: 50px; font-weight: 700; letter-spacing: 0.5px; }
  .offer-terms { font-size: 24px; line-height: 1.0; text-align: left; }
</style>
</head>
<body>
  <section class="billboard">
    <svg class="billboard-art" viewBox="0 0 1000 500" xmlns="http://www.w3.org/2000/svg">
      <defs>
        <linearGradient id="panelGradient" x1="0" y1="0" x2="1" y2="1">
          <stop offset="0" stop-color="#0a5fb4"/>
          <stop offset="0.55" stop-color="#1554a8"/>
          <stop offset="1" stop-color="#1c4596"/>
        </linearGradient>
        <linearGradient id="photoGradient" x1="0" y1="0" x2="1" y2="1">
          <stop offset="0" stop-color="#f1f0ec"/>
          <stop offset="0.35" stop-color="#9cc9e6"/>
          <stop offset="0.6" stop-color="#e7dcc6"/>
          <stop offset="0.85" stop-color="#f2d34a"/>
          <stop offset="1" stop-color="#ece6d8"/>
        </linearGradient>
      </defs>

      <rect class="panel-base" x="0" y="0" width="1000" height="500" fill="url(#panelGradient)"/>
      <polygon class="panel-facet" points="560,0 1000,0 1000,260" fill="#ffffff" opacity="0.05"/>
      <polygon class="panel-facet" points="700,500 1000,140 1000,500" fill="#0b2f80" opacity="0.18"/>
      <polygon class="panel-facet" points="420,0 620,0 800,500 560,500" fill="#0677ba" opacity="0.22"/>

      <polygon class="photo-area" role="img"
        aria-label="Photo: a smiling caregiver in light blue scrubs with a stethoscope stands behind an elderly man in a wheelchair holding a red book, in a bright living room with shelves and a yellow sofa"
        points="0,0 337,0 498,500 0,500" fill="url(#photoGradient)"/>

      <polyline class="frame-line-photo" points="353,18 27,18 27,482 470,482"
        fill="none" stroke="#ffffff" stroke-width="1.6" opacity="0.9"/>
      <polyline class="frame-line-panel" points="353,18 972,18 972,482 470,482"
        fill="none" stroke="#2a9be0" stroke-width="1.6" opacity="0.85"/>
    </svg>

    <p class="brand-name">Harbor Lane Home Aides</p>

    <h1 class="headline">It Pays<span class="line-two">to Care!</span></h1>

    <p class="mission">Empowering FRIENDS AND FAMILY to care for their loves ones at home.</p>

    <p class="offer">
      <span class="offer-lead">Eligible participants receive</span>
      <span class="offer-amount-row">
        <span class="offer-upto">up to</span>
        <span class="offer-amount">$15,000</span>
        <span class="offer-terms">a year,<br>tax free.</span>
      </span>
    </p>
  </section>
</body>
</html>
```